FOOD SUPPLEMENT FOR SOAR THROAT - TELVAROSE

I need a design for a food supplement product. The product is a formulation designed to combat bacteria that causes infections in the throat. Due to the fact that is a food supplment the design has to be away from the regular farmacy products. The design has to be elegant in the same time to shows the seriousness of the product. Need to have 3 pictograms for gluten , sugar and lactose free, the photo of the ingredients is an option. As colors yellow, orange, lime green and dark blue is preferable. In attached the dimensions of the box, the logo of the name of the product and the old box where the 3 pictograms Ithe ingredients are Murraya paniculata, Vitamin C, Malva sylvestris and Filipendula ulmaria. The title under the name is Food supplement in functional chewing gum and in italian Integratore alimentare in chewing gum funzionale.

Industry/Entity Type

pharmaceutical

Colors
0054AA
0677BA
7BADD7
CADEEF
E8F1F8
59FF00
82FF00
B8FF75
E3FFCB
F4FFEA
FFF300
FFF600
FEFA6F
FFFEC7
FFFEE8
F0912C
F2A743
F7CA91
FBE8D2
FDF5EE

Requirements
Must have
• pictograms -gluten, lactose, sugar free

```html
<!DOCTYPE html>
<html lang="en">
<head>
<meta charset="utf-8">
<title>TELVAROSE – Food supplement in functional chewing gum</title>
<link rel="stylesheet" href="https://fonts.googleapis.com/css2?family=Roboto+Condensed:ital,wght@0,800;1,700&family=Montserrat:wght@700&display=swap">
<style>
  :root {
    --stage: #e6e8e9;
    --navy-deep: #221f5e;
    --navy: #262a6e;
    --blue-glow: #0a74bf;
    --lime: #a3c937;
    --name-yellow: #d8e41c;
    --orange: #f0912c;
    --yellow: #ffd200;
    --white: #ffffff;
  }
  * { margin: 0; padding: 0; box-sizing: border-box; }
  html, body { width: 1200px; height: 939px; overflow: hidden; background: var(--stage); }
  .canvas { position: relative; width: 1200px; height: 939px; }
  .box-front {
    position: absolute; left: 50px; top: 125px; width: 1100px; height: 688px;
    overflow: hidden;
    background: radial-gradient(ellipse 560px 420px at 540px 330px, var(--blue-glow) 0%, #1a4e9c 45%, var(--navy) 80%, var(--navy-deep) 100%);
  }
  .artwork { position: absolute; inset: 0; width: 1100px; height: 688px; }
  .product-name {
    position: absolute; left: 205px; top: 146px; width: 420px;
    font-family: "Roboto Condensed", sans-serif; font-weight: 800; font-size: 88px;
    line-height: 1; letter-spacing: -1px; color: var(--name-yellow); text-align: center;
  }
  .claim {
    position: absolute; font-family: "Roboto Condensed", sans-serif;
    font-style: italic; font-weight: 700; white-space: nowrap; line-height: 1;
  }
  .claim-en { left: 127px; top: 381px; font-size: 29px; color: var(--navy-deep); }
  .claim-it { left: 122px; top: 429px; font-size: 25px; color: var(--white); }
  .badge-label { font-family: "Montserrat", sans-serif; font-weight: 700; font-size: 16px; fill: var(--navy-deep); letter-spacing: 0.5px; }
</style>
</head>
<body>
<main class="canvas">
  <section class="box-front">
    <svg class="artwork" viewBox="0 0 1100 688" xmlns="http://www.w3.org/2000/svg">
      <defs>
        <radialGradient id="photo-jasmine" cx="50%" cy="40%" r="60%">
          <stop offset="0" stop-color="#f4f6ee"/><stop offset="0.6" stop-color="#d9e2c8"/><stop offset="1" stop-color="#8fa56a"/>
        </radialGradient>
        <radialGradient id="photo-mallow" cx="55%" cy="55%" r="60%">
          <stop offset="0" stop-color="#8a2a78"/><stop offset="0.6" stop-color="#5b1d55"/><stop offset="1" stop-color="#263a22"/>
        </radialGradient>
        <radialGradient id="photo-meadowsweet" cx="50%" cy="55%" r="60%">
          <stop offset="0" stop-color="#eef0dc"/><stop offset="0.6" stop-color="#d6dcb8"/><stop offset="1" stop-color="#6f7e5a"/>
        </radialGradient>
        <path id="badge-arc" d="M -66 0 A 66 66 0 0 1 66 0"/>
      </defs>

      <path class="corner-swoosh" d="M0 0 H273 C140 20 40 100 0 213 Z" fill="var(--lime)"/>

      <g class="speed-lines">
        <polygon points="0,308 636,308 644,314 0,314" fill="var(--lime)"/>
        <polygon points="91,324 723,324 731,330 99,330" fill="var(--orange)"/>
        <polygon points="175,340 801,340 810,346 183,346" fill="var(--yellow)"/>
      </g>

      <polygon class="claim-band" points="0,377 758,377 746,414 0,414" fill="var(--lime)"/>

      <g class="ingredient-photos">
        <circle cx="168" cy="674" r="117" fill="url(#photo-jasmine)" role="img" aria-label="Photo of Murraya paniculata white flower"/>
        <circle cx="436" cy="674" r="117" fill="url(#photo-mallow)" role="img" aria-label="Photo of Malva sylvestris purple flowers"/>
        <circle cx="703" cy="674" r="117" fill="url(#photo-meadowsweet)" role="img" aria-label="Photo of Filipendula ulmaria cream blossoms"/>
      </g>

      <g class="free-badge sugar-free" transform="translate(970 141)">
        <circle r="77" fill="var(--lime)"/>
        <circle r="55" fill="var(--navy)"/>
        <text class="badge-label"><textPath href="#badge-arc" startOffset="50%" text-anchor="middle">SUGAR FREE</textPath></text>
        <g fill="none" stroke="var(--lime)" stroke-width="3" stroke-linejoin="round">
          <path d="M-28 0 l14 -7 14 7 v16 l-14 7 -14 -7 z M-28 0 l14 7 14 -7 M-14 7 v16"/>
          <path d="M0 0 l14 -7 14 7 v16 l-14 7 -14 -7 z M0 0 l14 7 14 -7 M14 7 v16"/>
          <path d="M-14 -16 l14 -7 14 7 v16 l-14 7 -14 -7 z M-14 -16 l14 7 14 -7 M0 -9 v16"/>
        </g>
        <line x1="42" y1="-42" x2="-42" y2="42" stroke="var(--lime)" stroke-width="9" stroke-linecap="round"/>
      </g>

      <g class="free-badge lactose-free" transform="translate(970 336)">
        <circle r="77" fill="var(--lime)"/>
        <circle r="55" fill="var(--navy)"/>
        <text class="badge-label"><textPath href="#badge-arc" startOffset="50%" text-anchor="middle">LACTOSE FREE</textPath></text>
        <path d="M-6 -34 h12 v10 l8 12 v40 h-28 v-40 l8 -12 z" fill="none" stroke="var(--lime)" stroke-width="3.5" stroke-linejoin="round"/>
        <line x1="42" y1="-42" x2="-42" y2="42" stroke="var(--lime)" stroke-width="9" stroke-linecap="round"/>
      </g>

      <g class="free-badge gluten-free" transform="translate(970 530)">
        <circle r="77" fill="var(--lime)"/>
        <circle r="55" fill="var(--navy)"/>
        <text class="badge-label"><textPath href="#badge-arc" startOffset="50%" text-anchor="middle">GLUTEN FREE</textPath></text>
        <g fill="none" stroke="var(--lime)" stroke-width="3.5" stroke-linecap="round">
          <line x1="0" y1="-30" x2="0" y2="34"/>
          <ellipse cx="0" cy="-26" rx="5" ry="9"/>
          <ellipse cx="-9" cy="-10" rx="5" ry="9" transform="rotate(-35 -9 -10)"/>
          <ellipse cx="9" cy="-10" rx="5" ry="9" transform="rotate(35 9 -10)"/>
          <ellipse cx="-9" cy="8" rx="5" ry="9" transform="rotate(-35 -9 8)"/>
          <ellipse cx="9" cy="8" rx="5" ry="9" transform="rotate(35 9 8)"/>
        </g>
        <line x1="42" y1="-42" x2="-42" y2="42" stroke="var(--lime)" stroke-width="9" stroke-linecap="round"/>
      </g>
    </svg>

    <h1 class="product-name">TELVAROSE</h1>
    <p class="claim claim-en">FOOD SUPPLEMENT IN FUNCTIONAL CHEWING GUM</p>
    <p class="claim claim-it">INTEGRATORE ALIMENTARE IN CHEWING GUM FUNZIONALE</p>
  </section>
</main>
</body>
</html>
```